ADA COMPLIANCE

We are in need of flyer or tri fold page for ada compliance, handicap ramps and parking lot striping.

Target Market(s)

Commercial Construction Industry

Industry/Entity Type

Parking

Font styles to use
Other font styles liked:
• Felix Titling

Colors
0355a3
acd036

Requirements
Must have
• Our Company Name and logo, 8004172593 number License #2837406
• List of services provided in uploaded images. Navy blue with high vizability green

```html
<!DOCTYPE html>
<html lang="en">
<head>
<meta charset="utf-8">
<title>Vanguard Paving Services – Tri Fold Brochure</title>
<link rel="stylesheet" href="https://fonts.googleapis.com/css2?family=Open+Sans:wght@400;600;700;800&family=Arimo:wght@400&display=swap">
<style>
  :root{
    --navy:#0a2b5e;
    --navy-deep:#06234f;
    --sky:#3f95ee;
    --bubble:#0d4fa0;
    --white:#ffffff;
    --hazard:#f2d21b;
    --page:#ece7de;
    --asphalt:#3b3f45;
  }
  *{box-sizing:border-box;margin:0;padding:0}
  html,body{width:1200px;height:730px;overflow:hidden;background:var(--page)}
  body{position:relative;font-family:"Open Sans",Arial,sans-serif;color:var(--white)}
  .sheet{position:absolute;top:137px;width:570px;height:456px;overflow:hidden;box-shadow:0 4px 14px rgba(0,0,0,.25)}
  .sheet--front{left:20px;background:var(--navy)}
  .sheet--inner{left:610px;background:var(--navy)}
  .block{position:absolute}
  .photo{position:absolute}
  .photo--building{background:linear-gradient(160deg,#b9c7d6 0%,#9aa3a8 55%,#c9c4b8 100%)}
  .photo--lot{background:linear-gradient(170deg,#7d8a96 0%,var(--asphalt) 40%,#2f4f86 100%)}
  .photo--ramp{background:linear-gradient(160deg,#8a6c52 0%,#9b9d9c 50%,#cfcfcc 100%)}
  .photo--field{background:linear-gradient(180deg,#a9b8c6 0%,#b7ab92 22%,#2e3237 30%,#3c4046 100%)}
  .photo--store{background:linear-gradient(180deg,#a9c8e6 0%,#c8a58a 40%,#3a3e45 62%,#2f4e8a 100%)}
  .photo--warehouse{background:linear-gradient(160deg,#55585c 0%,#6d6b56 60%,#4a4a40 100%)}
  .navy{background:var(--navy)}
  .sky{background:var(--sky)}
  .headline{font-weight:700;text-align:center;line-height:1.12}
  .headline__lead{font-size:13.5px;display:block}
  .headline__sub{font-size:12.5px;display:block}
  .phone-big{font-weight:700;font-size:24px;text-align:center}
  .brand{display:flex;flex-direction:column;align-items:center;justify-content:center;gap:6px;color:var(--navy)}
  .brand__mark{width:22px;height:22px;border-radius:50%;background:var(--navy)}
  .brand__name{font-weight:700;font-size:21px;letter-spacing:.5px;text-align:center;line-height:1.1}
  .license{font-weight:700;font-size:10px;text-align:center;line-height:18px}
  .tagline{font-family:"Arimo",Arial,sans-serif;text-align:center;line-height:1}
  .tagline__small{font-size:17px;display:block}
  .tagline__big{font-size:36px;display:block;margin-top:2px}
  .band{position:absolute;background:var(--hazard)}
  .cta{font-weight:700;font-size:17px;text-align:center;line-height:1.12}
  .list-title{font-weight:700;font-size:18px;line-height:24px;letter-spacing:.3px}
  .list-sub{font-weight:700;font-size:9.5px;line-height:13px;margin:1px 0 3px}
  .list{list-style:none}
  .list li{font-size:9.5px;line-height:12px;padding-left:10px;position:relative}
  .list li::before{content:"";position:absolute;left:0;top:4px;width:5px;height:5px;background:var(--white)}
  .list--small li{font-size:8.5px;line-height:11.5px}
</style>
</head>
<body>

<!-- Front of the brochure -->
<section class="sheet sheet--front" aria-label="Brochure front">
  <!-- Column one -->
  <div class="photo photo--building" role="img" aria-label="Photo of a building with a concrete accessible ramp and railings" style="left:0;top:0;width:190px;height:160px"></div>
  <div class="block navy" style="left:0;top:160px;width:190px;height:160px">
    <p class="headline" style="margin-top:22px"><span class="headline__lead">ADA COMPLIANCE</span><span class="headline__sub">Handicap Ramps and<br>Parking Lot Striping</span></p>
  </div>
  <div class="block sky" style="left:0;top:320px;width:190px;height:80px">
    <p class="phone-big" style="margin-top:36px">800 417 2593</p>
  </div>
  <svg class="block" style="left:30px;top:240px" width="130" height="100" viewBox="0 0 130 100" aria-label="Call now for no obligation quote">
    <path d="M70 88 L84 99 L82 84 Z" fill="var(--bubble)" stroke="#fff" stroke-width="1.5"/>
    <ellipse cx="65" cy="46" rx="62" ry="42" fill="var(--bubble)" stroke="#fff" stroke-width="1.5"/>
    <text x="65" y="34" text-anchor="middle" font-family="Open Sans, sans-serif" font-weight="700" font-size="15" fill="#fff">Call now for</text>
    <text x="65" y="52" text-anchor="middle" font-family="Open Sans, sans-serif" font-weight="700" font-size="15" fill="#fff">no obligation</text>
    <text x="65" y="70" text-anchor="middle" font-family="Open Sans, sans-serif" font-weight="700" font-size="15" fill="#fff">quote</text>
  </svg>

  <!-- Column two -->
  <div class="photo photo--lot" role="img" aria-label="Photo of a parking lot with blue accessible stalls and no parking markings" style="left:190px;top:0;width:190px;height:200px"></div>
  <div class="block sky" style="left:190px;top:200px;width:190px;height:85px">
    <p class="headline" style="margin-top:20px"><span class="headline__lead">ADA COMPLIANCE</span><span class="headline__sub">Handicap Ramps and<br>Parking Lot Striping</span></p>
  </div>
  <div class="photo photo--ramp" role="img" aria-label="Photo of a metal railed ramp beside a brick building" style="left:190px;top:285px;width:190px;height:171px"></div>

  <!-- Column three -->
  <div class="block sky brand" style="left:380px;top:0;width:190px;height:140px">
    <span class="brand__mark"></span>
    <span class="brand__name">VANGUARD PAVING<br>SERVICES INC</span>
  </div>
  <div class="block navy license" style="left:380px;top:140px;width:190px;height:18px">License #2837406</div>
  <div class="photo photo--lot" role="img" aria-label="Photo of freshly striped accessible parking stalls" style="left:380px;top:158px;width:190px;height:122px"></div>
  <div class="block navy" style="left:380px;top:280px;width:190px;height:90px">
    <p class="tagline" style="margin-top:18px"><span class="tagline__small">Feel Them</span><span class="tagline__big">Invited!</span></p>
  </div>
  <div class="photo photo--ramp" role="img" aria-label="Photo of a ramp railing near a building entrance" style="left:380px;top:370px;width:190px;height:86px"></div>
</section>

<!-- Inside of the brochure -->
<section class="sheet sheet--inner" aria-label="Brochure inner">
  <div class="photo photo--field" role="img" aria-label="Photo of a crew striping a new parking lot with a work truck" style="left:0;top:0;width:380px;height:235px"></div>
  <div class="band" style="left:0;top:235px;width:380px;height:10px"></div>
  <div class="block navy" style="left:0;top:245px;width:380px;height:75px;display:flex;align-items:center;justify-content:space-around">
    <p class="cta">Call now for<br>no obligation<br>quote</p>
    <p class="phone-big" style="font-size:23px">8004172593</p>
  </div>
  <div class="band" style="left:0;top:320px;width:380px;height:10px"></div>
  <div class="photo photo--lot" role="img" aria-label="Photo of a worker painting white parking lines" style="left:0;top:330px;width:190px;height:126px"></div>
  <div class="photo photo--warehouse" role="img" aria-label="Photo of yellow pallet striping on a warehouse floor" style="left:190px;top:330px;width:190px;height:126px"></div>

  <div class="block sky" style="left:380px;top:0;width:190px;height:182px;padding:12px 12px 0 14px">
    <h2 class="list-title">SERVICES</h2>
    <p class="list-sub">PARKING LOT STRIPING</p>
    <ul class="list">
      <li>Line Striping &amp; Stenciling</li>
      <li>Handicap ADA Striping</li>
      <li>Curb Painting</li>
      <li>Signs &amp; Poles</li>
      <li>Car Stops &amp; Bollards</li>
      <li>Game Courts</li>
      <li>Raised Pavement Markers</li>
      <li>Thermoplastics</li>
      <li>Pallet Striping</li>
    </ul>
  </div>
  <div class="photo photo--store" role="img" aria-label="Photo of a storefront lot with blue accessible parking stall" style="left:380px;top:182px;width:190px;height:148px"></div>
  <div class="block sky" style="left:380px;top:330px;width:190px;height:126px;padding:18px 10px 0 14px">
    <p class="list-sub" style="font-size:9px">PARKING LOT STRIPING IS</p>
    <ul class="list list--small">
      <li>Parking Lot lines</li>
      <li>Curbing</li>
      <li>Handicap Logos</li>
      <li>Fire Lanes and No Parking Zones</li>
      <li>Pretty much any marking<br>on a parking lot area.</li>
    </ul>
  </div>
</section>

</body>
</html>
```